ROOM REVIVE HQ
With Moira Pennell
Project: ROOM REVIVE HQ
ROOM REVIVE HQ -
Creative Brief
Use specific fonts
Not sure at the moment
Professional
Moira Pennell
Elmcroft Lodge 9 Elmcroft Terrace Hastings East Sussex TN37 6QR
moira@roomrevivehq.co.uk
www.roomrevivehq.co.uk
Company No. 5290418
Thinking of selling, about to reduce the price of your home? Before you do, speak to Moira Pennell at Room Revive HQ to see how Home Staging can help assist in selling your property fast and for the best asking price
Services Home Staging De Cluttering Moving in Moving out House Photography Sourcing accessorise

```html
<!DOCTYPE html>
<html lang="en">
<head>
<meta charset="utf-8">
<title>Room Revive HQ – Stationery Set</title>
<link href="https://fonts.googleapis.com/css2?family=Montserrat:wght@400;600;700&family=Great+Vibes&display=swap" rel="stylesheet">
<style>
  :root{
    --pink:#e4197d;
    --navy:#1c2a6e;
    --paper:#ffffff;
    --paper-shade:#eef0f4;
    --ink:#4a4f5c;
    --stage-top:#4a4a4a;
    --stage-bottom:#2d2d2d;
  }
  *{margin:0;padding:0;box-sizing:border-box}
  html,body{width:1200px;height:245px;overflow:hidden}
  body{
    position:relative;
    background:radial-gradient(ellipse at 50% 40%,var(--stage-top),var(--stage-bottom));
    font-family:"Montserrat",Arial,sans-serif;color:var(--ink);
  }
  .item{position:absolute;background:var(--paper);overflow:hidden;box-shadow:0 2px 4px rgba(0,0,0,.45)}
  .wave{position:absolute;left:0;bottom:0;width:100%}
  .brand{display:flex;align-items:center;gap:2px;color:var(--navy);font-weight:700;white-space:nowrap;line-height:1}
  .brand .dot{border-radius:50%;background:var(--pink);flex:none}
  .tiny{font-size:3.6px;line-height:1.45;white-space:nowrap}

  /* hero mark */
  .hero{position:absolute;left:14px;top:112px;width:94px;height:120px;display:flex;flex-direction:column;align-items:center;justify-content:center;gap:6px}
  .hero .dot{width:54px;height:54px;border-radius:50%;background:var(--pink)}
  .hero .name{color:var(--paper);font-weight:700;font-size:9px;text-align:center;line-height:1.2;white-space:nowrap}

  /* business cards */
  .card{width:93px;height:60px}
  .card.front .brand{position:absolute;left:6px;top:9px;width:32px;flex-direction:column;align-items:center;gap:3px;font-size:4.2px;white-space:normal;text-align:center;line-height:1.15}
  .card.front .brand .dot{width:10px;height:10px}
  .card .details{position:absolute;left:42px;top:9px}
  .card .details strong{color:var(--navy);font-size:4.4px;display:block;margin-bottom:1px}
  .card.back{display:flex;align-items:center;justify-content:center}
  .card.back .brand{font-size:6px}
  .card.back .brand .dot{width:10px;height:10px}
  .card.navy{background:var(--navy)}
  .card.navy .brand{color:var(--paper)}

  /* letterhead */
  .letter{left:336px;top:24px;width:139px;height:204px}
  .letter .brand{position:absolute;left:9px;top:10px;font-size:4.4px}
  .letter .brand .dot{width:9px;height:9px}
  .letter .contact{position:absolute;left:84px;top:9px}
  .watermark{position:absolute;left:50%;top:92px;transform:translate(-50%,-50%);display:flex;flex-direction:column;align-items:center;gap:4px;opacity:.12}
  .watermark .dot{width:42px;height:42px;border-radius:50%;background:var(--navy)}
  .watermark span{color:var(--navy);font-weight:700;font-size:8px;white-space:nowrap}
  .letter .footer{position:absolute;bottom:3px;width:100%;text-align:center;color:var(--paper);font-size:3.2px}

  /* continuation sheets */
  .sheet{width:96px}
  .sheet .brand{position:absolute;left:7px;top:8px;font-size:4.5px}
  .sheet .brand .dot{width:8px;height:8px}

  /* envelopes */
  .envelope{left:619px;width:173px;height:60px}
  .flap{position:absolute;left:0;top:0;width:100%;height:100%}
  .envelope .brand{position:absolute;left:50%;transform:translateX(-50%);font-size:5px}
  .envelope .brand .dot{width:8px;height:8px}

  /* compliments slip */
  .slip{left:828px;top:163px;width:360px;height:77px}
  .slip .brand{position:absolute;left:14px;top:12px;font-size:7px}
  .slip .brand .dot{width:12px;height:12px}
  .slip .script{position:absolute;right:26px;top:14px;font-family:"Great Vibes",cursive;font-size:21px;color:var(--navy);white-space:nowrap}
</style>
</head>
<body>

<svg width="0" height="0" style="position:absolute">
  <defs>
    <symbol id="wave-band" viewBox="0 0 100 20" preserveAspectRatio="none">
      <path d="M0 8 C30 0 60 16 100 4 L100 20 L0 20Z" fill="#e4197d"/>
      <path d="M0 13 C35 6 65 20 100 10 L100 20 L0 20Z" fill="#1c2a6e"/>
    </symbol>
  </defs>
</svg>

<div class="hero">
  <span class="dot"></span>
  <span class="name">ROOM REVIVE HQ</span>
</div>

<!-- business cards -->
<div class="item card front" style="left:120px;top:89px">
  <div class="brand"><span class="dot"></span>ROOM REVIVE HQ</div>
  <div class="details tiny"><strong>Moira Pennell</strong>Home Staging Consultant<br>moira@roomrevivehq.co.uk<br>www.roomrevivehq.co.uk</div>
  <svg class="wave" height="10"><use href="#wave-band"/></svg>
</div>
<div class="item card front" style="left:221px;top:89px">
  <div class="brand"><span class="dot"></span>ROOM REVIVE HQ</div>
  <div class="details tiny"><strong>Moira Pennell</strong>Elmcroft Lodge<br>9 Elmcroft Terrace<br>Hastings TN37 6QR</div>
  <svg class="wave" height="10"><use href="#wave-band"/></svg>
</div>
<div class="item card back" style="left:120px;top:160px">
  <div class="brand"><span class="dot"></span>ROOM REVIVE HQ</div>
  <svg class="wave" height="10"><use href="#wave-band"/></svg>
</div>
<div class="item card back navy" style="left:221px;top:160px">
  <div class="brand"><span class="dot"></span>ROOM REVIVE HQ</div>
</div>

<!-- letterhead -->
<div class="item letter">
  <div class="brand"><span class="dot"></span>ROOM REVIVE HQ</div>
  <div class="contact tiny">Elmcroft Lodge<br>9 Elmcroft Terrace<br>Hastings East Sussex<br>TN37 6QR<br>moira@roomrevivehq.co.uk<br>www.roomrevivehq.co.uk</div>
  <div class="watermark"><span class="dot"></span><span>ROOM REVIVE HQ</span></div>
  <svg class="wave" height="20"><use href="#wave-band"/></svg>
  <div class="footer">Company No. 5290418</div>
</div>

<!-- continuation sheets -->
<div class="item sheet" style="left:492px;top:96px;height:66px">
  <div class="brand"><span class="dot"></span>ROOM REVIVE HQ</div>
  <svg class="wave" height="9"><use href="#wave-band"/></svg>
</div>
<div class="item sheet" style="left:492px;top:168px;height:54px">
  <svg class="wave" height="9"><use href="#wave-band"/></svg>
</div>

<!-- envelopes -->
<div class="item envelope" style="top:41px">
  <svg class="flap" viewBox="0 0 173 60" preserveAspectRatio="none">
    <path d="M0 0 H173 V12 L86.5 30 L0 12Z" fill="var(--pink)"/>
  </svg>
  <div class="brand" style="top:19px;color:var(--paper)"><span class="dot" style="background:var(--paper)"></span>ROOM REVIVE HQ</div>
  <svg class="wave" height="8"><use href="#wave-band"/></svg>
</div>
<div class="item envelope" style="top:108px">
  <svg class="flap" viewBox="0 0 173 60" preserveAspectRatio="none">
    <path d="M0 0 H173 V12 L86.5 30 L0 12Z" fill="var(--navy)"/>
  </svg>
  <div class="brand" style="top:19px;color:var(--paper)"><span class="dot"></span>ROOM REVIVE HQ</div>
  <svg class="wave" height="8"><use href="#wave-band"/></svg>
</div>
<div class="item envelope" style="top:178px;background:var(--paper-shade)">
  <svg class="flap" viewBox="0 0 173 57" preserveAspectRatio="none">
    <path d="M0 0 L86.5 30 L173 0" fill="var(--paper)" stroke="#c9ccd4" stroke-width=".6"/>
    <path d="M0 57 L86.5 26 L173 57" fill="none" stroke="#c9ccd4" stroke-width=".6"/>
  </svg>
</div>

<!-- compliments slip -->
<div class="item slip">
  <div class="brand"><span class="dot"></span>ROOM REVIVE HQ</div>
  <div class="script">With Compliments</div>
  <svg class="wave" height="12"><use href="#wave-band"/></svg>
</div>

</body>
</html>
```